Torvel, Inc. new buisness cards - brand guide included

We need new business cards. SLEAK SIMPLE FINANCE. They must include a place for NAME, TITLE, CELL, OFFICE PHONE, EMAIL. they also must include our services across the bottom. AIR, OCEAN, FTL, LTL, EXPRESS. for reference this will be being handed to some of the most prestigious shipping companies in a america.

Target Market(s)

Finance and corporate

Contact Information for Business Card

We need new business cards. SLEAK SIMPLE FINANCE. They must include a place for NAME, TITLE, CELL, OFFICE PHONE, EMAIL. they also must include our services across the bottom. AIR, OCEAN, FTL, LTL, EXPRESS.

Requirements
Must have
• We need new business cards. SLEAK SIMPLE FINANCE. They must include a place for NAME, TITLE, CELL, OFFICE PHONE, EMAIL. they also must include our services across the bottom. AIR, OCEAN, FTL, LTL, EXPRESS.
Nice to have
• USE THE COLORS AND LOGO IN THE BRAND GUIDE :)

```html
<!DOCTYPE html>
<html lang="en">
<head>
<meta charset="utf-8">
<title>Torvel, Inc. Business Card</title>
<link href="https://fonts.googleapis.com/css2?family=Montserrat:wght@300;400;500;600;700&display=swap" rel="stylesheet">
<style>
  :root {
    --backdrop: #d6d3ce;
    --card-black: #1c1c1c;
    --card-white: #fbfbfa;
    --gold: #b9a77e;
    --gold-deep: #a89466;
    --silver: #c9c9c9;
    --ink: #3a3a3a;
    --ink-soft: #5c5c5c;
    --rule: #8a8a8a;
  }
  * { margin: 0; padding: 0; box-sizing: border-box; }
  html, body {
    width: 1200px; height: 975px; overflow: hidden;
    background: var(--backdrop);
    font-family: "Montserrat", sans-serif;
  }
  .stage {
    position: relative; width: 1200px; height: 975px;
  }
  .card {
    position: absolute; left: 280px;
    width: 640px; height: 366px;
    border-radius: 3px;
    box-shadow: 0 10px 28px rgba(0,0,0,0.18);
    overflow: hidden;
  }
  /* Front */
  .card-front {
    top: 100px;
    background: var(--card-black);
    border-bottom: 4px solid var(--gold);
  }
  .front-mark {
    position: absolute; top: 120px; left: 0; width: 100%;
    text-align: center;
    font-weight: 400; font-size: 66px; letter-spacing: 10px;
    color: var(--silver);
  }
  .services {
    position: absolute; top: 262px; left: 0; width: 100%;
    text-align: center; list-style: none;
    font-size: 14px; font-weight: 500; letter-spacing: 1.5px;
    color: #e8e8e8;
  }
  .services li { display: inline; }
  .services li::before {
    content: "\2022"; color: var(--gold); margin: 0 5px 0 8px;
  }
  /* Back */
  .card-back {
    top: 509px;
    background: var(--card-white);
  }
  .side-band {
    position: absolute; top: 0; left: 0; width: 26px; height: 100%;
    background: var(--gold);
    border-right: 4px solid #222;
    box-shadow: 4px 0 0 #fff;
  }
  .back-mark {
    position: absolute; top: 44px; right: 56px;
    display: flex; align-items: center; gap: 10px;
    font-weight: 400; font-size: 36px; letter-spacing: 5px;
    color: var(--gold);
  }
  .back-mark .dot {
    width: 12px; height: 12px; background: var(--gold);
  }
  .divider {
    position: absolute; top: 120px; left: 88px; right: 56px;
    height: 1px; background: var(--rule);
  }
  .address {
    position: absolute; top: 140px; right: 56px;
    text-align: right; font-style: normal;
    font-size: 14px; line-height: 1.45; color: var(--ink-soft);
  }
  .person { position: absolute; top: 140px; left: 88px; }
  .person-name {
    font-size: 20px; font-weight: 700; letter-spacing: 1px;
    color: var(--gold-deep); text-transform: uppercase;
  }
  .person-title { font-size: 16px; color: var(--ink-soft); margin-top: 2px; }
  .contacts {
    position: absolute; top: 222px; left: 88px; list-style: none;
    font-size: 14px; color: var(--ink); line-height: 1.6;
  }
  .contacts li { display: flex; align-items: center; gap: 10px; }
  .contacts svg { width: 13px; height: 13px; fill: var(--gold); }
</style>
</head>
<body>
<main class="stage">
  <section class="card card-front" aria-label="Card front">
    <div class="front-mark">TORVEL</div>
    <ul class="services">
      <li>AIR</li><li>OCEAN</li><li>FTL</li><li>LTL</li><li>EXPRESS.</li>
    </ul>
  </section>

  <section class="card card-back" aria-label="Card back">
    <div class="side-band"></div>
    <div class="back-mark"><span class="dot"></span>TORVEL</div>
    <div class="divider"></div>
    <address class="address">
      Torvel, Inc.<br>
      2210 Harbor Loop NE<br>
      Ste 410 Lakeview<br>
      WA 98100
    </address>
    <div class="person">
      <h1 class="person-name">Daniel Herrick</h1>
      <p class="person-title">Managing Director</p>
    </div>
    <ul class="contacts">
      <li>
        <svg viewBox="0 0 16 16" aria-hidden="true"><path d="M3 1h3l1.5 4-2 1.3a9 9 0 0 0 4.2 4.2L11 8.5l4 1.5v3c0 1-1 2-2 2C6.4 15 1 9.6 1 3c0-1 1-2 2-2z"/></svg>
        555.214.0187
      </li>
      <li>
        <svg viewBox="0 0 16 16" aria-hidden="true"><path d="M4 0h8a1 1 0 0 1 1 1v14a1 1 0 0 1-1 1H4a1 1 0 0 1-1-1V1a1 1 0 0 1 1-1zm1 2v10h6V2zm3 11a1 1 0 1 0 0 2 1 1 0 0 0 0-2z"/></svg>
        555.390.4412
      </li>
      <li>
        <svg viewBox="0 0 16 16" aria-hidden="true"><path d="M1 3h14v10H1zm1.5 1.2V5l5.5 4 5.5-4v-.8z"/></svg>
        dan@torvelmail.com
      </li>
      <li>
        <svg viewBox="0 0 16 16" aria-hidden="true"><path d="M8 1a7 7 0 1 0 0 14A7 7 0 0 0 8 1zm0 1.5c.8 1 1.4 2.5 1.6 4.5H6.4C6.6 5 7.2 3.5 8 2.5zM6.4 9h3.2c-.2 2-.8 3.5-1.6 4.5C7.2 12.5 6.6 11 6.4 9z"/></svg>
        www.torvelfreight.com
      </li>
    </ul>
  </section>
</main>
</body>
</html>
```